QR TILL WORKS , CREDIT CARD PROCESSING EQUIPMENT

qrtillworks is a sub division of Tallow a credit car processing co.
harold finch
14 cedar hollow ln
hollis bay 07312
suite 412

qrtillworks.example
cell 555-214-7730
office 555-861-2093
we sell pos systems to merchant who want to accept credit cards at there retail location.
black card would be nice buit open to different ideas

Target Market(s)

retail merchants

Industry/Entity Type

credit card processing

Contact Information for Business Card

card should include web site phone address

Colors

Designer to choose colors to be used in the design.

Requirements
Should not have
• red

```html
<!DOCTYPE html>
<html lang="en">
<head>
<meta charset="utf-8">
<title>QR TILL WORKS — Business Card</title>
<link rel="stylesheet" href="https://fonts.googleapis.com/css2?family=Arimo:wght@400;700&display=swap">
<style>
  :root {
    --backdrop: #1c1c1c;
    --card-black: #030303;
    --card-sheen: #262626;
    --accent: #f2c10f;
    --ink-light: #ffffff;
    --ink-soft: #e6e6e6;
  }
  * { margin: 0; padding: 0; box-sizing: border-box; }
  html, body {
    width: 1200px; height: 900px; overflow: hidden;
    background: var(--backdrop);
    font-family: "Arimo", Arial, sans-serif;
  }
  .stage {
    width: 1200px; height: 900px;
    display: flex; flex-direction: column; align-items: center; justify-content: center;
    gap: 44px;
  }
  .card {
    position: relative;
    width: 640px; height: 366px;
    background: var(--card-black);
    overflow: hidden;
    box-shadow: 0 14px 30px rgba(0,0,0,.55);
  }
  .card__sheen {
    position: absolute; top: 0; right: 0; bottom: 0; width: 48%;
    background: linear-gradient(90deg, var(--card-black) 0%, var(--card-sheen) 18%, #1a1a1a 100%);
  }
  .card__edge {
    position: absolute; left: 0; right: 0; bottom: 0; height: 10px;
    background: var(--accent);
  }
  .brand {
    position: absolute;
    display: flex; align-items: center; gap: 14px;
    color: var(--ink-light);
    font-weight: 700;
    letter-spacing: 0.04em;
    white-space: nowrap;
  }
  .brand__dot {
    width: 18px; height: 18px; border-radius: 50%;
    background: var(--accent);
    flex: none;
  }
  .card--front .brand { left: 118px; top: 150px; font-size: 44px; }
  .card--back .brand { left: 38px; top: 162px; font-size: 23px; gap: 9px; }
  .card--back .brand__dot { width: 12px; height: 12px; }
  .divider {
    position: absolute; left: 300px; top: 38px; bottom: 48px; width: 2px;
    background: var(--accent);
  }
  .contact {
    position: absolute; left: 338px; top: 44px; right: 20px;
    color: var(--ink-soft);
  }
  .contact__name {
    color: var(--accent); font-weight: 700; font-size: 26px; letter-spacing: .01em;
  }
  .contact__role { font-size: 14px; margin-top: 4px; color: var(--ink-light); }
  .icon {
    width: 20px; height: 20px; border-radius: 50%;
    background: var(--accent);
    display: inline-flex; align-items: center; justify-content: center;
  }
  .icon svg { width: 12px; height: 12px; }
  .contact__address { margin-top: 28px; font-size: 14px; line-height: 1.3; }
  .contact__address .icon { margin-bottom: 8px; }
  .contact__icons { display: flex; gap: 12px; margin-top: 20px; }
  .contact__lines { margin-top: 10px; font-size: 14px; line-height: 1.32; }
</style>
</head>
<body>
<main class="stage">
  <section class="card card--front" aria-label="Card front">
    <div class="card__sheen"></div>
    <div class="brand"><span class="brand__dot"></span>QR TILL WORKS</div>
    <div class="card__edge"></div>
  </section>

  <section class="card card--back" aria-label="Card back">
    <div class="card__sheen"></div>
    <div class="brand"><span class="brand__dot"></span>QR TILL WORKS</div>
    <div class="divider"></div>
    <div class="contact">
      <div class="contact__name">Dorian Pell</div>
      <div class="contact__role">Director</div>
      <div class="contact__address">
        <span class="icon"><svg viewBox="0 0 12 12"><path d="M6 1a3.2 3.2 0 0 0-3.2 3.2C2.8 6.6 6 11 6 11s3.2-4.4 3.2-6.8A3.2 3.2 0 0 0 6 1zm0 4.4a1.2 1.2 0 1 1 0-2.4 1.2 1.2 0 0 1 0 2.4z" fill="#111"/></svg></span>
        <div>14 cedar hollow ln</div>
        <div>hollis bay 07312 suite 412</div>
      </div>
      <div class="contact__icons">
        <span class="icon"><svg viewBox="0 0 12 12"><path d="M3 1.5l1.6 2.2-.9 1.1c.6 1.3 1.6 2.3 2.9 2.9l1.1-.9 2.2 1.6-.8 1.8C5.6 10.3 1.7 6.4 1.5 2.3z" fill="#111"/></svg></span>
        <span class="icon"><svg viewBox="0 0 12 12"><rect x="3.5" y="1" width="5" height="10" rx="1" fill="none" stroke="#111" stroke-width="1.2"/><circle cx="6" cy="9.3" r=".6" fill="#111"/></svg></span>
        <span class="icon"><svg viewBox="0 0 12 12"><rect x="1.5" y="3" width="9" height="6" fill="none" stroke="#111" stroke-width="1.1"/><path d="M1.5 3L6 6.6 10.5 3" fill="none" stroke="#111" stroke-width="1.1"/></svg></span>
        <span class="icon"><svg viewBox="0 0 12 12" fill="none" stroke="#111" stroke-width="1"><circle cx="6" cy="6" r="4.5"/><ellipse cx="6" cy="6" rx="2" ry="4.5"/><path d="M1.5 6h9"/></svg></span>
      </div>
      <div class="contact__lines">
        <div>555-861-2093</div>
        <div>555-214-7730</div>
        <div>info@qrtillworks.example</div>
        <div>www.qrtillworks.example</div>
      </div>
    </div>
    <div class="card__edge"></div>
  </section>
</main>
</body>
</html>
```